Audio/ Video Packaging Design for a Technology company.

We need a packaging design for a bag that is 7" wide and 10" high. The design will be for a new line of audio/video products. We would like to see designs that represent a superior quality product that provides a pure connection. We want the equivalent of a nice retail bag that you would find in a store like Tallow Mart. It should be a maximum of three colors. We really want something sharp, professional and eye catching, not whimsical or cartoonish. I've included a couple of examples below. I don't really like the designs of the bags, but I want you to see examples of what I'm looking for.

The company logo, which is uploaded, should be on the design. The words "audio and video products" should be either underneath the logo or to the side. Also, somewhere on the bag, we would like the words "For a Pure Connection"

The winner of this contest will likely get the opportunity for additional work as we have more products ready to launch.

Target Market(s)

resellers, consumers - men 25-60

Industry/Entity Type

It Company

Requirements
Must have
• It should be a maximum of three colors. We really want something sharp, professional and eye catching, not whimsical or cartoonish
Nice to have
• Eye-catching design. Utilize the entire bag but don't make it too busy.
Should not have
• Whimsical, cartoonish

```html
<!DOCTYPE html>
<html lang="en">
<head>
<meta charset="utf-8">
<title>Veltrix Audio and Video Products – Bag Packaging</title>
<link rel="stylesheet" href="https://fonts.googleapis.com/css2?family=Exo+2:wght@400;500&family=Fira+Sans+Extra+Condensed:wght@500&display=swap">
<style>
  :root {
    --bg-top: #1a78b8;
    --bg-light: #3aa0dc;
    --bg-deep: #22406a;
    --bg-bottom: #1c5f91;
    --bag-blue: #1f7fc2;
    --bag-blue-dark: #1a4f92;
    --panel-light: #1e8fd0;
    --panel-dark: #174f8f;
    --ink-navy: #1b2a5a;
    --ink-blue: #1f4a9a;
    --white: #ffffff;
    --glow: rgba(190, 235, 255, 0.85);
    --art-light: #36aef0;
    --art-dark: #1d3f8f;
  }
  * { box-sizing: border-box; margin: 0; padding: 0; }
  html, body { width: 1200px; height: 787px; overflow: hidden; }
  body {
    position: relative;
    background: linear-gradient(180deg, var(--bg-top) 0%, var(--bg-light) 24%, #2b6da8 50%, var(--bg-deep) 78%, var(--bg-bottom) 100%);
    font-family: "Exo 2", sans-serif;
  }
  .bag {
    position: absolute;
    top: 118px;
    width: 430px;
    height: 614px;
    border-radius: 26px;
    background: linear-gradient(135deg, var(--bag-blue) 0%, var(--bag-blue-dark) 100%);
    box-shadow: 0 0 18px 4px var(--glow), 0 0 2px 2px rgba(255,255,255,0.7);
  }
  .bag--front { left: 152px; }
  .bag--back { left: 618px; }
  .bag__panel {
    position: absolute;
    left: 21px;
    top: 21px;
    width: 388px;
    border-radius: 20px 20px 0 0;
  }
  .bag--front .bag__panel {
    height: 543px;
    background: linear-gradient(90deg, #f4f4f4 0%, #ffffff 6%, #ffffff 92%, #ececec 100%);
  }
  .bag--back .bag__panel {
    height: 555px;
    background: linear-gradient(160deg, var(--panel-light) 0%, #1a72b8 45%, var(--panel-dark) 100%);
    box-shadow: inset 0 0 10px rgba(0,0,0,0.15);
  }
  .bag__seal {
    position: absolute;
    left: 21px;
    width: 388px;
    top: 88px;
    height: 16px;
    border-top: 2px solid rgba(0,0,0,0.07);
    border-bottom: 2px solid rgba(0,0,0,0.07);
  }
  .bag__seal::after {
    content: "";
    position: absolute;
    left: 0; right: 0; top: 5px;
    border-top: 2px solid rgba(0,0,0,0.06);
  }
  .bag--back .bag__seal,
  .bag--back .bag__seal::after { border-color: rgba(10,40,90,0.45); }
  .bag__tab {
    position: absolute;
    left: 92px;
    top: 0;
    width: 246px;
    height: 114px;
    border-radius: 0 0 22px 22px;
    background: linear-gradient(135deg, #1f7fc4 0%, var(--bag-blue-dark) 100%);
  }
  .bag--back .bag__tab { background: linear-gradient(135deg, #1c6fb4 0%, #1a5196 100%); }
  .bag__hanger {
    position: absolute;
    left: 72px;
    top: 36px;
    width: 102px;
    height: 20px;
    border-radius: 10px;
    background: var(--white);
  }
  .bag__hanger::before {
    content: "";
    position: absolute;
    left: 41px;
    top: -7px;
    width: 20px;
    height: 14px;
    border-radius: 10px 10px 0 0;
    background: var(--white);
  }
  .brand {
    position: absolute;
    left: 0;
    width: 430px;
    text-align: center;
  }
  .brand__name {
    display: inline-flex;
    align-items: center;
    gap: 14px;
    font-size: 46px;
    font-weight: 500;
    letter-spacing: 2px;
    line-height: 1;
  }
  .brand__dot {
    width: 30px;
    height: 30px;
    border-radius: 50%;
  }
  .brand__tagline {
    margin-top: 10px;
    padding-left: 30px;
    font-size: 20px;
    font-weight: 400;
    line-height: 1;
  }
  .bag--front .brand { top: 138px; }
  .bag--front .brand__name { color: var(--ink-navy); }
  .bag--front .brand__dot { background: var(--art-light); }
  .bag--front .brand__tagline { color: var(--ink-navy); }
  .bag--front .brand__tagline span { color: var(--ink-blue); }
  .bag--back .brand { top: 141px; }
  .bag--back .brand__name,
  .bag--back .brand__tagline { color: var(--white); }
  .bag--back .brand__dot { background: var(--white); }
  .connector-art {
    position: absolute;
    border-radius: 50% / 40%;
    background: radial-gradient(ellipse at center, var(--art-dark) 0%, #2a7fd0 45%, var(--art-light) 75%, rgba(54,174,240,0) 100%);
  }
  .bag--front .connector-art { left: 48px; top: 446px; width: 334px; height: 96px; }
  .bag--back .connector-art { left: 106px; top: 506px; width: 218px; height: 60px; }
  .slogan {
    position: absolute;
    left: 0;
    width: 430px;
    top: 568px;
    text-align: center;
    font-family: "Fira Sans Extra Condensed", sans-serif;
    font-weight: 500;
    font-size: 28px;
    color: var(--white);
  }
  .compliance {
    position: absolute;
    left: 0;
    width: 430px;
    top: 584px;
    display: flex;
    justify-content: center;
    align-items: center;
    gap: 8px;
    font-family: "Fira Sans Extra Condensed", sans-serif;
    font-weight: 500;
    font-size: 13px;
    color: var(--white);
  }
  .compliance__mark { display: block; }
</style>
</head>
<body>
  <section class="bag bag--front" aria-label="Front of bag">
    <div class="bag__panel"></div>
    <div class="bag__seal"></div>
    <div class="bag__tab"><div class="bag__hanger"></div></div>
    <div class="brand">
      <div class="brand__name"><span class="brand__dot"></span>VELTRIX</div>
      <p class="brand__tagline">Audio and Video <span>Products</span></p>
    </div>
    <div class="connector-art" role="img" aria-label="Blue 3D chevron band illustration suggesting a connection"></div>
    <p class="slogan">For a Pure Connection</p>
  </section>

  <section class="bag bag--back" aria-label="Back of bag">
    <div class="bag__panel"></div>
    <div class="bag__seal"></div>
    <div class="bag__tab"><div class="bag__hanger"></div></div>
    <div class="brand">
      <div class="brand__name"><span class="brand__dot"></span>VELTRIX</div>
      <p class="brand__tagline">Audio and Video Products</p>
    </div>
    <div class="connector-art" role="img" aria-label="Small blue 3D chevron band illustration"></div>
    <div class="compliance">
      <span>MADE IN CHINA</span>
      <svg class="compliance__mark" width="26" height="16" viewBox="0 0 26 16" aria-hidden="true"><rect x="1" y="1" width="24" height="14" rx="2" fill="none" stroke="#fff" stroke-width="2"/></svg>
      <svg class="compliance__mark" width="18" height="18" viewBox="0 0 18 18" aria-hidden="true"><circle cx="9" cy="9" r="8" fill="#fff"/></svg>
      <svg class="compliance__mark" width="18" height="18" viewBox="0 0 18 18" aria-hidden="true"><circle cx="9" cy="9" r="7" fill="none" stroke="#fff" stroke-width="2.5"/></svg>
    </div>
  </section>
</body>
</html>
```